Velmora Biz Card 2019

New business card for Velmora Property Inspections. We are a residential home inspection company in Arizona.

Target Market(s)

Real Estate

Font styles to use
Sans Serif

Requirements
Must have
• Glen Mirewick
• Home Inspector
• Velmora Property Inspections, LLC
• 480-555-0172
• glen@velmora-llc.example

```html
<!DOCTYPE html>
<html lang="en">
<head>
<meta charset="utf-8">
<title>Velmora Property Inspections – Business Card</title>
<link rel="stylesheet" href="https://fonts.googleapis.com/css2?family=Arimo:wght@400;700&display=swap">
<style>
  :root {
    --page-bg: #ececec;
    --card-white: #ffffff;
    --card-mist: #e4e5e6;
    --brand-green: #3bb54a;
    --brand-green-dark: #2e9d3c;
    --ink-grey: #6d6e70;
    --ink-dark: #58595b;
    --slate: #636466;
    --slate-light: #727375;
    --silver: #d4d5d7;
  }
  * { margin: 0; padding: 0; box-sizing: border-box; }
  html, body {
    width: 1200px;
    height: 1200px;
    overflow: hidden;
    background: var(--page-bg);
    font-family: "Arimo", Arial, sans-serif;
  }
  .canvas {
    position: relative;
    width: 1200px;
    height: 1200px;
  }
  .card {
    position: absolute;
    left: 220px;
    width: 760px;
    height: 456px;
    overflow: hidden;
  }
  .card--front {
    top: 144px;
    background: linear-gradient(160deg, var(--card-mist) 0%, var(--card-white) 45%, #f3f3f4 100%);
  }
  .card--back {
    top: 648px;
    background: linear-gradient(150deg, var(--slate-light) 0%, var(--slate) 60%, #5d5e60 100%);
  }
  .card__waves {
    position: absolute;
    inset: 0;
    width: 760px;
    height: 456px;
  }

  /* Brand name block */
  .brand {
    position: absolute;
    display: flex;
    align-items: center;
    gap: 12px;
    font-weight: 700;
    letter-spacing: 2px;
  }
  .brand__mark {
    width: 22px;
    height: 22px;
  }
  .card--front .brand {
    left: 80px;
    top: 190px;
    font-size: 44px;
    color: var(--ink-grey);
  }
  .card--front .brand__mark { background: var(--brand-green); }
  .card--back .brand {
    left: 0;
    right: 0;
    top: 200px;
    justify-content: center;
    font-size: 52px;
    color: var(--silver);
  }
  .card--back .brand__mark { background: var(--silver); width: 26px; height: 26px; }

  .divider {
    position: absolute;
    left: 376px;
    top: 86px;
    width: 2px;
    height: 232px;
    background: var(--ink-grey);
  }

  .contact {
    position: absolute;
    left: 406px;
    top: 78px;
    color: var(--ink-grey);
  }
  .contact__name {
    font-size: 29px;
    font-weight: 700;
    color: var(--brand-green);
    line-height: 1.1;
  }
  .contact__title {
    font-size: 22px;
    line-height: 1.3;
    margin-bottom: 26px;
  }
  .contact__company {
    font-size: 15.5px;
    font-weight: 700;
    line-height: 1.4;
  }
  .contact__address {
    font-size: 19px;
    line-height: 1.38;
    font-style: normal;
    margin-bottom: 8px;
  }
  .contact__list { list-style: none; }
  .contact__item {
    display: flex;
    align-items: center;
    gap: 8px;
    font-size: 18px;
    line-height: 1.42;
  }
  .contact__icon {
    width: 13px;
    height: 13px;
    fill: var(--brand-green);
    flex: none;
  }
</style>
</head>
<body>
<main class="canvas">

  <section class="card card--front" aria-label="Business card front">
    <svg class="card__waves" viewBox="0 0 760 456" aria-hidden="true">
      <path d="M0,368 C200,440 440,436 640,350 C470,430 220,448 0,404 Z" fill="var(--brand-green)"/>
      <path d="M0,412 C200,452 520,430 760,280 L760,456 L0,456 Z" fill="var(--slate)"/>
    </svg>

    <div class="brand">
      <span class="brand__mark"></span>
      <span class="brand__name">VELMORA</span>
    </div>

    <div class="divider"></div>

    <div class="contact">
      <h1 class="contact__name">Glen Mirewick</h1>
      <p class="contact__title">Home Inspector</p>
      <p class="contact__company">Velmora Property Inspections, LLC</p>
      <address class="contact__address">4410 S. Harlow Ln.<br>Tempe, AZ 85290</address>
      <ul class="contact__list">
        <li class="contact__item">
          <svg class="contact__icon" viewBox="0 0 16 16" aria-hidden="true"><path d="M3.5 1 L6 1 L7 5 L5.3 6.3 C6.2 8.2 7.8 9.8 9.7 10.7 L11 9 L15 10 L15 12.5 C15 14 13.8 15 12.5 15 C6.5 14.6 1.4 9.5 1 3.5 C1 2.2 2 1 3.5 1 Z"/></svg>
          480-555-0172
        </li>
        <li class="contact__item">
          <svg class="contact__icon" viewBox="0 0 16 16" aria-hidden="true"><path d="M1 3 H15 V13 H1 Z M1.5 3.5 L8 9 L14.5 3.5" stroke="#fff" stroke-width="1.2"/></svg>
          glen@velmora-llc.example
        </li>
        <li class="contact__item">
          <svg class="contact__icon" viewBox="0 0 16 16" aria-hidden="true"><circle cx="8" cy="8" r="7"/><path d="M1 8 H15 M8 1 C5 4 5 12 8 15 M8 1 C11 4 11 12 8 15" stroke="#fff" stroke-width="1" fill="none"/></svg>
          www.velmora-llc.example
        </li>
      </ul>
    </div>
  </section>

  <section class="card card--back" aria-label="Business card back">
    <div class="brand">
      <span class="brand__mark"></span>
      <span class="brand__name">VELMORA</span>
    </div>
  </section>

</main>
</body>
</html>
```